Print Ad Redesign for Fine Art Auction Company

We need a new and improved newspaper ad. We need a full page and a strip version of the ad. We sell fine art and need a new attention grabbing ad. We put on auction events weekly all around the country of Australia. We want people to perceive the event as urgent to attend. We also want the audience to feel as though they will get great deals. Lastly, the ad should ultimately portray our company in a professional manner and display the luxurious quality of the items we sell.
Updates

Project Deadline Extended Reason: We would love to see more creative variations. We are looking for a design that incorporates the message but looks new, fresh, and different. Thank you! Added Saturday, April 16, 2016

Industry/Entity Type

It Company

Font styles to use
Serif
Sans Serif

Requirements
Must have
• See attached documents. Use those as inspiration. New fonts and features. Must incorporate the same orange colour.
Nice to have
• A completely fresh and new design that pops with attention grabbing features and design.
Should not have
• na

```html
<!DOCTYPE html>
<html lang="en">
<head>
<meta charset="utf-8">
<title>Whitlow's Fine Art Auctions – Major Art Auction</title>
<link rel="stylesheet" href="https://fonts.googleapis.com/css2?family=Roboto+Slab:wght@400;600;700;800;900&display=swap">
<style>
  :root {
    --orange: #f08322;
    --ink: #141414;
    --wall: #eceef0;
    --wall-light: #f7f8f9;
    --frame: #f4f4f4;
    --frame-edge: #d8dadc;
    --white: #ffffff;
    --wire: #8c9094;
  }
  * { margin: 0; padding: 0; box-sizing: border-box; }
  html, body { width: 1200px; height: 1000px; overflow: hidden; background: var(--white); }
  body { font-family: "Roboto Slab", Georgia, serif; color: var(--ink); position: relative; }

  .ad { position: absolute; left: 0; top: 78px; width: 1200px; height: 847px;
        background: radial-gradient(ellipse at 45% 35%, var(--wall-light) 0%, var(--wall) 80%); overflow: hidden; }

  .wires { position: absolute; left: 0; top: 0; width: 1200px; height: 250px; }

  .headline { position: absolute; left: 0; width: 1200px; text-align: center; text-transform: uppercase; line-height: 1; }
  .headline-top { top: 36px; font-size: 74px; font-weight: 900; letter-spacing: -1px; color: var(--ink); }
  .headline-main { top: 104px; font-size: 104px; font-weight: 800; letter-spacing: -1px; color: var(--orange); }

  .frame { position: absolute; top: 242px; width: 226px; height: 328px; background: var(--frame);
           border: 1px solid var(--frame-edge); box-shadow: 2px 4px 10px rgba(0,0,0,.12); }
  .frame-left { left: 226px; }
  .frame-centre { left: 499px; }
  .frame-right { left: 772px; }
  .artwork { position: absolute; left: 33px; top: 34px; width: 158px; height: 258px; }
  .art-portrait { background: linear-gradient(160deg, #b88650 0%, #9a8a78 45%, #7f9db5 80%, #a6b9c8 100%); }
  .art-feathers { background: linear-gradient(180deg, #3fb3a8 0%, #d45a7a 22%, #7ec46a 42%, #e0b35a 58%, #d96b8a 75%, #4a8fd0 100%); }
  .art-dots { background: linear-gradient(150deg, #e0643a 0%, #3a8fc8 30%, #e8a232 55%, #c93c3c 78%, #5aa0d8 100%); }

  .info { position: absolute; top: 626px; border-left: 4px solid var(--orange); padding-left: 10px; }
  .info-event { left: 62px; }
  .info-offer { left: 610px; width: 530px; }
  .tagline { font-size: 20px; font-weight: 700; color: var(--orange); text-transform: uppercase; line-height: 24px; }
  .venue { font-size: 19px; font-weight: 700; line-height: 24px; }
  .when { font-size: 12.5px; font-weight: 700; text-transform: uppercase; line-height: 18px; }
  .offer-copy { font-size: 13px; font-weight: 400; line-height: 15px; }
  .extras { font-size: 20px; font-weight: 700; color: var(--orange); text-transform: uppercase; line-height: 26px; margin-top: 2px; }

  .footer-band { position: absolute; left: 0; top: 740px; width: 1200px; height: 107px; background: var(--orange); }
  .contact { position: absolute; left: 50px; top: 24px; color: var(--white); font-weight: 700; }
  .contact-web { font-size: 20px; line-height: 26px; }
  .contact-phone { font-size: 28px; line-height: 34px; }
  .payment { position: absolute; left: 428px; top: 32px; width: 420px; text-align: center; color: var(--ink); }
  .payment-main { font-size: 20px; font-weight: 700; line-height: 24px; }
  .payment-note { font-size: 12.5px; font-weight: 700; line-height: 18px; }
  .brand { position: absolute; left: 950px; top: 40px; display: flex; align-items: center; gap: 10px;
           font-size: 24px; font-weight: 700; color: var(--ink); letter-spacing: 1px; }
  .brand-mark { width: 14px; height: 14px; background: var(--ink); }
</style>
</head>
<body>
<main class="ad">
  <svg class="wires" viewBox="0 0 1200 250" aria-hidden="true">
    <g stroke="var(--wire)" stroke-width="1">
      <line x1="250" y1="0" x2="250" y2="242"/>
      <line x1="428" y1="0" x2="428" y2="242"/>
      <line x1="523" y1="0" x2="523" y2="242"/>
      <line x1="700" y1="0" x2="700" y2="242"/>
      <line x1="796" y1="0" x2="796" y2="242"/>
      <line x1="974" y1="0" x2="974" y2="242"/>
    </g>
  </svg>

  <h1 class="headline headline-top">Tomorrow Major</h1>
  <h2 class="headline headline-main">Art Auction</h2>

  <div class="frame frame-left"><div class="artwork art-portrait" role="img" aria-label="Painting of a woman with long dark hair on a gold and blue background with flowers"></div></div>
  <div class="frame frame-centre"><div class="artwork art-feathers" role="img" aria-label="Abstract painting of colourful feather-like brush strokes"></div></div>
  <div class="frame frame-right"><div class="artwork art-dots" role="img" aria-label="Aboriginal dot painting with concentric circles in orange, red and blue"></div></div>

  <section class="info info-event">
    <p class="tagline">Art Liquidation ! Vendors in Distress</p>
    <p class="venue">Harbour Point Club, 14 Marina Bay Dr, NEDLANDS</p>
    <p class="when">Tomorrow Sunday 21 February • Auction 11:30am • Preview from 10am</p>
  </section>

  <section class="info info-offer">
    <p class="offer-copy">All artworks expected to sell for a fraction of retail price. Owning a masterpiece is within your reach. The biggest names in Australian, Aboriginal and European art. Incredible collection and variety.</p>
    <p class="extras">Bronze Sculptures • Handmade Carpets</p>
  </section>

  <footer class="footer-band">
    <div class="contact">
      <p class="contact-web">www.whitlows.com.au</p>
      <p class="contact-phone">Call 0412 380 516</p>
    </div>
    <div class="payment">
      <p class="payment-main">All cards, cash, cheque and EFTPOS.</p>
      <p class="payment-note">Catalogue descriptions guaranteed. Items subject to change.</p>
    </div>
    <div class="brand"><span class="brand-mark"></span>WHITLOW'S</div>
  </footer>
</main>
</body>
</html>
```